Financial services referral site needs a redesign

We need a complete re-brand ; new word press design for our existing site. Need a web 2.0 clean crisp look that will convert highly. Consumers with debt come to our site so we can refer them to 3rd party providers of debt solutions ranging from credit counseling, debt consolidation, refinance and student loan consolidation. I would like to see designs that use the color green and final product should communicate safety, trust and privacy. Show case our A+ QFR rating etc. See current site at pinegroveloanaid.com

- I would like to use light blue color scheme to match the logo. The green is making it look off - I definitely need the lead form to be on the top right side of the page

```html
<!DOCTYPE html>
<html lang="en">
<head>
<meta charset="utf-8">
<title>Pine Grove Loan Aid</title>
<link href="https://fonts.googleapis.com/css2?family=Open+Sans:ital,wght@0,400;0,600;0,700;1,400&family=Ubuntu:wght@500;700&display=swap" rel="stylesheet">
<style>
:root{
  --blue:#1a7fc4;
  --blue-dark:#0e6fb3;
  --sky:#5aa9d6;
  --orange:#f26c16;
  --text:#222;
  --muted:#555;
  --band:#e2e2e2;
  --panel-light:#8a8a8a;
  --panel-dark:#5a5a5a;
  --soft:#f5f5f5;
  --footer:#2b2b2b;
  --border:#cfcfcf;
}
*{box-sizing:border-box;margin:0;padding:0}
html,body{width:952px;height:1200px;overflow:hidden}
body{position:relative;background:#fff;font-family:"Open Sans",Arial,sans-serif;color:var(--text)}
.abs{position:absolute}
.top-band{left:0;top:0;width:952px;height:364px;background:var(--band)}
.brand{left:100px;top:36px;display:flex;align-items:center;gap:8px}
.brand-dot{width:44px;height:44px;border-radius:50%;background:var(--sky)}
.brand-name{font-size:19px;color:var(--blue);font-weight:400}
.nav{top:47px;left:479px;display:flex;gap:30px;font-size:13.5px}
.nav a{color:var(--blue);text-decoration:none;padding:2px 4px}
.nav a.active{color:#222;border:2px solid #999;background:#eee}
.arrow{top:190px;width:30px;height:35px;background:#bdbdbd}
.hero-photo{left:99px;top:107px;width:463px;height:339px;background:linear-gradient(135deg,#d9dde2 0%,#b9c2cc 45%,#8d8a84 80%,#c9a98a 100%)}
.dots{left:119px;top:427px;display:flex;gap:3px}
.dots span{width:4px;height:4px;border-radius:50%;background:#555}
.dots span.on{background:#c0282f}
.lead{left:562px;top:91px;width:296px;height:380px;background:linear-gradient(160deg,var(--panel-dark),var(--panel-light) 45%,var(--panel-dark));box-shadow:0 12px 24px rgba(0,0,0,.18)}
.lead-banner{left:571px;top:147px;width:293px;height:38px;background:linear-gradient(#4f6b80,#35526a);color:#fff;font-family:Ubuntu,sans-serif;font-weight:500;font-size:25px;text-align:center;line-height:38px;text-shadow:0 2px 2px rgba(0,0,0,.4)}
.lead-sub{left:562px;top:195px;width:296px;text-align:center;color:#fff;font-family:Ubuntu,sans-serif;font-weight:500;font-size:18px;line-height:24px;text-shadow:0 1px 2px rgba(0,0,0,.5)}
.field{background:#fff;border:1px solid #ccc;font-style:italic;font-size:11px;color:#444;padding:0 9px;line-height:25px;height:27px}
.field.select::after{content:"";position:absolute;right:10px;top:11px;border:5px solid transparent;border-top:6px solid #333}
.cta{left:604px;top:403px;width:214px;height:41px;background:var(--orange);color:#fff;font-size:14px;font-weight:600;text-align:center;line-height:41px}
.intro-title{top:515px;left:0;width:952px;text-align:center;font-size:17.5px;font-weight:400}
.intro-text{top:553px;left:205px;width:542px;text-align:center;font-size:10.4px;line-height:20px;color:#333}
.card{top:700px;width:239px;height:171px;border:2px solid #d6d6d6;background:#fff;padding:10px 18px}
.card h3{color:var(--blue);font-weight:400;font-size:16px;line-height:21.5px;text-align:center;margin:0 -12px 9px}
.card p{font-size:8px;line-height:15px;color:#444;max-width:180px}
.card p.wide{max-width:none;font-size:7.5px;line-height:12px}
.btn{position:absolute;left:20px;bottom:12px;background:var(--blue-dark);color:#fff;font-size:10px;width:76px;height:21px;line-height:21px;text-align:center}
.badge{display:flex;gap:6px;margin:0 0 12px 76px}
.badge-shape{width:30px;height:46px;background:#1b5f96;border-radius:2px}
.badge-text{font-size:7.5px;font-weight:700;color:#1b5f96;text-align:center;line-height:10px;padding-top:6px}
.ticks{list-style:none;font-size:8.5px;color:#555;line-height:17.5px;padding-left:12px}
.ticks li svg{vertical-align:-1px;margin-right:3px}
.lower{left:0;top:925px;width:952px;height:212px;background:var(--soft);border-top:1px solid #e5e5e5}
.lower-title{top:948px;color:var(--blue);font-weight:400;font-size:16.5px}
.q-input{left:246px;width:159px;border:2px solid var(--blue);background:#fff;font-style:italic;font-size:11px;color:#888;padding:2px 5px}
.news-item{left:493px;width:215px;display:flex;gap:14px}
.date{font-size:8.5px;text-align:center;width:20px;flex:none}
.date b{display:block;background:var(--blue);color:#fff;font-size:8.5px;margin-top:3px;line-height:11px}
.news-body h4{font-weight:400;font-size:8px;margin-bottom:4px}
.news-body p{font-size:6.5px;line-height:9.7px;color:#666}
.news-body a{color:var(--blue);text-decoration:none}
.footer{left:0;top:1137px;width:952px;height:63px;background:var(--footer);color:#eee;font-size:9.5px}
.copy{left:100px;top:26px}
.social{right:100px;top:24px;display:flex;gap:4px}
.social span{width:15px;height:15px}
</style>
</head>
<body>
<div class="abs top-band"></div>

<div class="abs brand"><span class="brand-dot"></span><span class="brand-name">Pine Grove Loan Aid</span></div>
<nav class="abs nav"><a class="active">Home</a><a>Debt Consolidation</a><a>About Us</a><a>Contact Us</a></nav>

<div class="abs arrow" style="left:0"><svg width="30" height="35"><path d="M18 10 L10 17.5 L18 25" stroke="#fff" stroke-width="4" fill="none"/></svg></div>
<div class="abs arrow" style="left:922px"><svg width="30" height="35"><path d="M12 10 L20 17.5 L12 25" stroke="#fff" stroke-width="4" fill="none"/></svg></div>

<div class="abs hero-photo" role="img" aria-label="Photo of two business consultants reviewing a laptop at a desk"></div>
<div class="abs dots"><span></span><span class="on"></span><span></span><span></span></div>

<div class="abs lead"></div>
<div class="abs lead-banner">Unlimited Possibilites</div>
<div class="abs lead-sub">Our Debt Solutions<br>Can Help You</div>
<div class="abs field" style="left:601px;top:258px;width:219px">Name</div>
<div class="abs field" style="left:601px;top:302px;width:103px">Phone</div>
<div class="abs field" style="left:712px;top:302px;width:108px">Email</div>
<div class="abs field select" style="left:601px;top:345px;width:103px">State</div>
<div class="abs field select" style="left:712px;top:345px;width:108px">Debt Amount</div>
<div class="abs cta">Get Assistance Now</div>

<h1 class="abs intro-title">When To Consider A Debt Consolidation Program</h1>
<p class="abs intro-text">In today’s economy, it is very common for consumer’s to find themselves overwhelmed by credit card debt and in need of debt reduction. Consumers who need more than basic budgeting to pay off debts and are having difficulties making their monthly payments should consider a debt consolidation program in order to get back on track. A debt consolidation program, also known as a debt management program, is the process of consolidating unsecured credit card debt into one monthly payment, often with lower interest rates.</p>

<section class="abs card" style="left:100px">
  <h3>GET OUT OF DEBT NOW -<br>LIVE BETTER!</h3>
  <p>Since 2006, we have helped thousands of consumers get out of debt. Fill out the free no obligation form above and take your first step towards financial freedom and peace of mind.</p>
  <span class="btn">Learn more</span>
</section>
<section class="abs card" style="left:356px">
  <h3>See our Rating</h3>
  <div class="badge"><span class="badge-shape"></span><span class="badge-text">QFR Rating:<br>A+</span></div>
  <p class="wide">Lorem ipsum is a dummy text only. Dolor sit amet, consectetur adipiscing elit.</p>
  <span class="btn">Learn more</span>
</section>
<section class="abs card" style="left:613px">
  <h3>Act now to take advantage<br>of the following benefits</h3>
  <ul class="ticks">
    <li><svg width="8" height="8"><path d="M1 4 L3 6.5 L7 1.5" stroke="#555" stroke-width="1.8" fill="none"/></svg>Reduce high interest credit rates</li>
    <li><svg width="8" height="8"><path d="M1 4 L3 6.5 L7 1.5" stroke="#555" stroke-width="1.8" fill="none"/></svg>Stop harassing credit calls</li>
    <li><svg width="8" height="8"><path d="M1 4 L3 6.5 L7 1.5" stroke="#555" stroke-width="1.8" fill="none"/></svg>One low monthly payment</li>
    <li><svg width="8" height="8"><path d="M1 4 L3 6.5 L7 1.5" stroke="#555" stroke-width="1.8" fill="none"/></svg>No costs unless you save</li>
  </ul>
  <span class="btn">Learn more</span>
</section>

<div class="abs lower"></div>
<h2 class="abs lower-title" style="left:256px">Ask Us A Question</h2>
<div class="abs q-input" style="top:983px;height:23px">Name</div>
<div class="abs q-input" style="top:1014px;height:23px">Email</div>
<div class="abs q-input" style="top:1044px;height:65px">Your message</div>

<h2 class="abs lower-title" style="left:497px">Current Debt Relief News</h2>
<article class="abs news-item" style="top:984px">
  <div class="date">July<b>26</b></div>
  <div class="news-body"><h4>Credit Debt Relief: Understand Your Options</h4><p>Credit debt relief can be achieved in a number of ways. Generally, this may involve debt consolidation, debt settlement, bankruptcy and credit counseling....<br><a>[Read more]</a></p></div>
</article>
<article class="abs news-item" style="top:1054px">
  <div class="date">July<b>26</b></div>
  <div class="news-body"><h4>Credit Debt Relief: Understand Your Options</h4><p>Credit debt relief can be achieved in a number of ways. Generally, this may involve debt consolidation, debt settlement, bankruptcy and credit counseling....<br><a>[Read more]</a></p></div>
</article>

<footer class="abs footer">
  <span class="abs copy">Copyright©Pine Grove Loan Aid 2014. All Rights Reserved.</span>
  <div class="abs social" aria-label="Social links">
    <span style="background:#1da1f2"></span><span style="background:#0e76a8"></span><span style="background:#dd4b39"></span><span style="background:#3b5998"></span>
  </div>
</footer>
</body>
</html>
```